Mirabo & Orvan Automotive Repair Shop. Need a new website design.

We specialize in Mirabo & Orvan auto repair, but also work on other Asian import vehicles. We have been in business for 7 years and pride ourselves on high quality auto repair that is fixed right the first time. Would like the automotive repair website to incorporate the colors black, red and white if possible and have our logo and some Mirabo and Orvan vehicles included in the website.

Target Market(s)

Mirabo & Orvan vehicle owners

Industry/Entity Type

Automotive Repair

Coding

Coded - Design and coding required

Number of Pages Required

5+ page

Colors
EB3D1F
EC4F4E
F09395
F8D3D4
FCEDEE

Requirements
Must have
• Home, Services, Contact Us, Schedule appointment, and a gallery tab that I can add shop pictures to when completed.
Nice to have
• Would like to see example pictures of job next to each service listed.
Should not have
• Service not related to auto repair. Ex. auto detailing, towing, car wash

```html
<!DOCTYPE html>
<html lang="en">
<head>
<meta charset="utf-8">
<title>Halden Automotive — Mirabo, Orvan &amp; Kestra Auto Repair</title>
<link href="https://fonts.googleapis.com/css2?family=Oswald:wght@500;600;700&family=Poppins:ital,wght@0,400;0,500;0,600;1,400&display=swap" rel="stylesheet">
<style>
:root{
  --red:#eb3d1f;
  --red-soft:#ec4f4e;
  --white:#ffffff;
  --ink:#0d0d0d;
  --panel:#151515;
  --card:#1b1b1b;
  --muted:#cfcfcf;
  --line:#2a2a2a;
}
*{margin:0;padding:0;box-sizing:border-box}
html,body{width:1200px;height:4890px;overflow:hidden;background:var(--ink);color:var(--white);font-family:"Poppins",sans-serif}
.page{position:relative;width:1200px;height:4890px}
.abs{position:absolute}
.ph{position:absolute}
.display{font-family:"Oswald",sans-serif;font-weight:600;text-transform:uppercase;letter-spacing:.5px;line-height:1.05}
.eyebrow{font-size:18px;color:var(--red);text-transform:uppercase;font-weight:500}
.eyebrow.lined::before{content:"";display:inline-block;width:80px;height:2px;background:var(--red);vertical-align:middle;margin-right:14px}
.btn{position:absolute;display:flex;align-items:center;justify-content:center;background:var(--red);color:var(--white);font-size:15px;font-weight:600;text-transform:uppercase;border-radius:3px}
.btn.ghost{background:transparent;border:2px solid var(--white)}
.btn.outline-red{background:transparent;border:2px solid var(--red);color:var(--red)}

/* nav */
.hero{top:0;left:0;width:1200px;height:627px;background:radial-gradient(ellipse at 60% 30%,#3a3a3a,#1a1a1a 70%)}
.brand{position:absolute;display:flex;align-items:center;gap:10px;font-family:"Oswald",sans-serif;font-weight:700;font-size:30px;color:var(--white)}
.brand .mark{width:22px;height:22px;border-radius:50%;background:var(--red)}
.nav{position:absolute;top:34px;left:392px;display:flex;gap:48px;font-size:15px;font-weight:500}
.nav a{color:var(--white);text-decoration:none}
.nav a.active{color:var(--red);border-bottom:2px solid var(--red);padding-bottom:6px}
.talk{top:26px;left:968px;width:132px;height:42px;background:transparent;border:2px solid var(--red);font-size:14px}
.hero h1{top:230px;left:99px;font-size:44px}
.hero .sub{top:342px;left:99px;font-family:"Oswald",sans-serif;font-size:19px;font-weight:500}

/* about */
.about{top:627px;left:0;width:1200px;height:684px;background:#121212}
.about p{top:247px;left:657px;width:443px;font-size:15.5px;line-height:31.5px;text-align:justify;color:#e6e6e6}

/* services */
.services{top:1311px;left:0;width:1200px;height:728px;background:#111}
.center{left:0;width:1200px;text-align:center}
.svc-card{position:absolute;top:199px;width:236px;height:366px;background:var(--card)}
.svc-card .ph{top:0;left:0;width:236px;height:163px}
.svc-card .badge{position:absolute;top:134px;left:88px;width:60px;height:60px;border-radius:50%;background:var(--red);border:3px solid var(--white)}
.svc-card h3{position:absolute;top:212px;width:100%;text-align:center;font-size:19px;font-weight:600}
.svc-card p{position:absolute;top:244px;left:14px;width:208px;text-align:center;font-size:13.5px;line-height:25px;color:#e0e0e0}
.svc-card .arrow{position:absolute;top:324px;left:104px}

/* band */
.band{top:2039px;left:0;width:1200px;height:511px}
.band .h1{top:92px;left:99px;font-family:"Oswald",sans-serif;font-weight:700;font-style:italic;font-size:56px;line-height:62px}
.band .h2{top:222px;left:99px;font-size:50px;line-height:60px}

/* news */
.news{top:2550px;left:0;width:1200px;height:737px;background:#121212}
.post{position:absolute;top:192px;width:315px;height:469px;background:var(--card)}
.post .ph{top:0;left:0;width:315px;height:209px}
.post .date{position:absolute;top:183px;right:16px;width:40px;height:52px;background:var(--red);text-align:center;font-family:"Oswald",sans-serif;font-size:24px;line-height:28px;border:2px solid var(--white)}
.post .date small{display:block;font-size:12px;line-height:14px}
.post .meta{position:absolute;top:222px;left:16px;font-size:13.5px;color:var(--red)}
.post h3{position:absolute;top:250px;left:16px;font-size:19px;font-weight:600}
.post p{position:absolute;top:290px;left:16px;width:286px;font-size:13.5px;line-height:27px;color:#e0e0e0}
.post .btn{top:416px;left:16px;width:140px;height:34px;font-size:13px}

/* testimonials */
.reviews{top:3287px;left:0;width:1200px;height:481px;background:linear-gradient(90deg,#6e3414,#2a1a12 45%,#1e1e1e 60%)}
.review-list{top:204px;left:657px;width:460px}
.quote{font-size:15px;font-style:italic;line-height:28px}
.who{font-size:18px;font-weight:600;line-height:28px;margin-top:6px;margin-bottom:12px}

/* contact */
.contact{top:3768px;left:0;width:1200px;height:503px;background:linear-gradient(90deg,#4a4a44,#2c2d2c 60%,#3a3a38)}

/* newsletter */
.newsletter{top:4271px;left:0;width:1200px;height:289px;background:#121212}
.field-label{font-size:13px}
.field{position:absolute;height:38px;background:var(--white);color:#333;font-size:14px;padding:10px 12px;border-radius:2px}

/* footer */
.footer{top:4560px;left:0;width:1200px;height:330px;background:#111}
.fcol h4{font-family:"Oswald",sans-serif;font-size:17px;font-weight:600;margin-bottom:14px;text-transform:uppercase}
.fcol li{list-style:none;font-size:15px;line-height:31px}
.info li{display:flex;gap:8px;align-items:flex-start;line-height:22px;margin-bottom:9px}
.social{position:absolute;top:4829px;width:38px;height:38px;border-radius:50%;background:var(--white);border:6px solid var(--red)}
</style>
</head>
<body>
<div class="page">

  <section class="abs hero">
    <div class="ph" role="img" aria-label="Red Mirabo sedan in a dark studio" style="top:180px;left:470px;width:700px;height:350px;background:radial-gradient(ellipse at center,#a0141a,#5a0c0e 45%,transparent 70%)"></div>
    <div class="brand" style="top:40px;left:99px"><span class="mark"></span>HALDEN</div>
    <nav class="nav">
      <a class="active">HOME</a><a>ABOUT US</a><a>SERVICES</a><a>BLOG</a><a>CONTACT US</a>
    </nav>
    <div class="btn talk">LET'S TALK</div>
    <h1 class="abs display">Dealership Quality at<br>Affordable Prices</h1>
    <div class="abs sub">Specializing in Mirabo, Orvan, &amp; Kestra Auto Repair</div>
    <div class="btn" style="top:395px;left:99px;width:270px;height:40px">Schedule an Appointment</div>
  </section>

  <section class="abs about">
    <svg class="abs" style="top:135px;left:140px" width="380" height="345"><polyline points="330,2 378,2 378,80" fill="none" stroke="#eb3d1f" stroke-width="2"/><polyline points="3,270 3,343 92,343" fill="none" stroke="#eb3d1f" stroke-width="2"/></svg>
    <div class="ph" role="img" aria-label="Dark Mirabo pickup truck with headlights on, outdoors" style="top:85px;left:99px;width:374px;height:413px;background:linear-gradient(160deg,#4a4e46,#1f2320)"></div>
    <div class="ph" role="img" aria-label="Mechanic working on an engine with a wrench" style="top:272px;left:232px;width:359px;height:344px;background:linear-gradient(140deg,#5a6470,#262b31);border:3px solid var(--white)">
      <svg class="abs" style="left:272px;top:262px" width="48" height="48"><circle cx="24" cy="24" r="21" fill="#000" stroke="#fff" stroke-width="2"/><polygon points="19,14 33,24 19,34" fill="#fff"/></svg>
    </div>
    <div class="abs eyebrow lined" style="top:136px;left:657px">About Us</div>
    <div class="abs display" style="top:170px;left:657px;font-size:50px">Halden Automotive</div>
    <p class="abs">Here at Halden Automotive, we believe in professional service and high quality auto repairs. With over 20 years of Mirabo, Orvan, &amp; Kestra dealership experience, we have all the tools, equipment, and knowledge to keep your Mirabo, Orvan, &amp; Kestra vehicle running strong. Although we specialize in these makes, we also repair &amp; service other import makes like Hoshiro, Aveno, Nakari, Ilvane, Korin, Hanvel, Mitsura, etc.</p>
    <div class="btn" style="top:523px;left:657px;width:157px;height:38px">Learn More</div>
  </section>

  <section class="abs services">
    <div class="abs center eyebrow" style="top:22px">Our Services</div>
    <div class="abs center display" style="top:54px;font-size:50px">What We Offer</div>
    <div class="abs center" style="top:118px;font-size:14.5px;line-height:22px">Don't see the service you think you need? Contact us anyway! This list is not<br>comprehensive of everything we're capable of!</div>
    <svg class="abs" style="top:367px;left:62px" width="16" height="28"><polyline points="14,2 2,14 14,26" fill="none" stroke="#ccc" stroke-width="2"/></svg>
    <svg class="abs" style="top:367px;left:1121px" width="16" height="28"><polyline points="2,2 14,14 2,26" fill="none" stroke="#ccc" stroke-width="2"/></svg>

    <div class="svc-card" style="left:101px">
      <div class="ph" role="img" aria-label="Engine being lifted out of a car in a workshop" style="background:linear-gradient(150deg,#8c8f94,#3b3e43)"></div>
      <div class="badge"></div><h3>Engine Replacement</h3>
      <p>Lorem ipsmet,etur adipiscing elit, ssmod tempor incididunt ut labore et dolore</p>
      <svg class="arrow" width="28" height="12"><path d="M0 6H26M20 1L26 6L20 11" fill="none" stroke="#fff" stroke-width="1.6"/></svg>
    </div>
    <div class="svc-card" style="left:355px">
      <div class="ph" role="img" aria-label="Mechanic inspecting a brake disc" style="background:linear-gradient(150deg,#6d6f73,#2c2d30)"></div>
      <div class="badge"></div><h3>Brakes</h3>
      <p>Lorem ipsmet,etur adipiscing elit, ssmod tempor incididunt ut labore et dolore</p>
      <svg class="arrow" width="28" height="12"><path d="M0 6H26M20 1L26 6L20 11" fill="none" stroke="#fff" stroke-width="1.6"/></svg>
    </div>
    <div class="svc-card" style="left:609px">
      <div class="ph" role="img" aria-label="Close view of an open engine block with seals" style="background:linear-gradient(150deg,#9a9a9a,#3a3a3a)"></div>
      <div class="badge"></div><h3>Front Engine Seals</h3>
      <p>Lorem ipsmet,etur adipiscing elit, ssmod tempor incididunt ut labore et dolore</p>
      <svg class="arrow" width="28" height="12"><path d="M0 6H26M20 1L26 6L20 11" fill="none" stroke="#fff" stroke-width="1.6"/></svg>
    </div>
    <div class="svc-card" style="left:863px">
      <div class="ph" role="img" aria-label="Wheel alignment clamp mounted on a car wheel" style="background:linear-gradient(150deg,#a3a6ab,#45484c)"></div>
      <div class="badge"></div><h3>Alignments</h3>
      <p>Lorem ipsmet,etur adipiscing elit, ssmod tempor incididunt ut labore et dolore</p>
      <svg class="arrow" width="28" height="12"><path d="M0 6H26M20 1L26 6L20 11" fill="none" stroke="#fff" stroke-width="1.6"/></svg>
    </div>
    <div class="btn" style="top:596px;left:522px;width:156px;height:40px">View More</div>
  </section>

  <section class="abs band" role="img" aria-label="Mechanic in goggles leaning over an open engine bay in a garage" style="background:linear-gradient(90deg,#121a22 30%,#2a3a4c 55%,#3b4756)">
    <div class="abs h1">Texas Largest Car<br>Care Facility</div>
    <div class="abs h2"><span style="color:var(--red)">Automotive</span> Hub<br>for Enthusiasts</div>
    <div class="btn" style="top:368px;left:99px;width:157px;height:40px">Learn More</div>
    <div class="btn ghost" style="top:368px;left:270px;width:156px;height:40px">Contact Us</div>
  </section>

  <section class="abs news">
    <div class="abs center eyebrow" style="top:70px">Resources</div>
    <div class="abs center display" style="top:102px;font-size:52px">Latest News &amp; Blogs</div>

    <article class="post" style="left:99px">
      <div class="ph" role="img" aria-label="Timing gear and engine parts on a workbench" style="background:linear-gradient(150deg,#6b7076,#25282c)"></div>
      <div class="date">01<small>FEB</small></div>
      <div class="meta">23 Comments &nbsp;|&nbsp; by John Doe</div>
      <h3>Finibus Bonorum et Malorum</h3>
      <p>Lorem ipsum dolor sit amet, consectetur adipiscing elit, sepor incididunt ut labore et dolore magna alis ipsum suspendisse ultrices gravida.</p>
      <div class="btn outline-red">More Info</div>
    </article>
    <article class="post" style="left:443px">
      <div class="ph" role="img" aria-label="Gloved hands servicing an engine with a tool" style="background:linear-gradient(150deg,#4c5e7a,#1d2430)"></div>
      <div class="date">01<small>FEB</small></div>
      <div class="meta">23 Comments &nbsp;|&nbsp; by John Doe</div>
      <h3>Finibus Bonorum et Malorum</h3>
      <p>Lorem ipsum dolor sit amet, consectetur adipiscing elit, sepor incididunt ut labore et dolore magna alis ipsum suspendisse ultrices gravida.</p>
      <div class="btn outline-red">More Info</div>
    </article>
    <article class="post" style="left:787px">
      <div class="ph" role="img" aria-label="Service advisor reviewing paperwork with customers in a shop" style="background:linear-gradient(150deg,#8a8c90,#3e3f43)"></div>
      <div class="date">01<small>FEB</small></div>
      <div class="meta">23 Comments &nbsp;|&nbsp; by John Doe</div>
      <h3>Finibus Bonorum et Malorum</h3>
      <p>Lorem ipsum dolor sit amet, consectetur adipiscing elit, sepor incididunt ut labore et dolore magna alis ipsum suspendisse ultrices gravida.</p>
      <div class="btn outline-red">More Info</div>
    </article>
  </section>

  <section class="abs reviews" role="img" aria-label="Mechanic working under warm light on an engine">
    <div class="abs eyebrow lined" style="top:104px;left:657px">Reviews</div>
    <div class="abs display" style="top:138px;left:655px;font-size:50px">Testimonials</div>
    <div class="abs review-list">
      <p class="quote">I would highly recommend Halden Automotive to family, friends, &amp; co-workers! I'm a repeat customer myself!</p>
      <p class="who">-Daniel R.</p>
      <p class="quote">Halden Automotive is my go to car repair company. I trust them with all my vehicle needs.</p>
      <p class="who">-Marisa K.</p>
    </div>
  </section>

  <section class="abs contact">
    <div class="ph" role="img" aria-label="Dark Orvan sedan parked at dusk" style="top:40px;left:520px;width:680px;height:460px;background:radial-gradient(ellipse at 65% 60%,#23262a,#2e302f 55%,transparent 75%)"></div>
    <div class="abs eyebrow lined" style="top:120px;left:99px">Let'stalk</div>
    <div class="abs display" style="top:154px;left:99px;font-size:50px">Get In Touch</div>
    <div class="abs" style="top:226px;left:99px;width:480px;font-size:15.5px;line-height:32px">Sed ut perspiciatis undnis iste natus error sit voluptatem accusantium dolorque laudantium, totam rem aperiam, eaque ipsa quae ab illo inventore veritatis</div>
    <div class="btn" style="top:338px;left:99px;width:157px;height:40px">Contact Us</div>
  </section>

  <section class="abs newsletter">
    <div class="abs center display" style="top:60px;font-size:42px">Sign Up to the Newsletter Today</div>
    <div class="abs field-label" style="top:138px;left:198px">NAME</div>
    <div class="abs field-label" style="top:138px;left:515px">EMAIL ADDRESS</div>
    <div class="field" style="top:163px;left:198px;width:300px">John Doe</div>
    <div class="field" style="top:163px;left:515px;width:300px">John Doe</div>
    <div class="btn" style="top:163px;left:828px;width:175px;height:38px">Subscribe</div>
  </section>

  <footer class="abs footer">
    <div class="brand" style="top:80px;left:99px;font-size:42px"><span class="mark" style="width:30px;height:30px"></span>HALDEN</div>
    <div class="abs fcol" style="top:30px;left:393px"><h4>Quick Links</h4><ul><li>Home</li><li>About Us</li><li>Services</li><li>Blog</li><li>Contact Us</li></ul></div>
    <div class="abs fcol" style="top:30px;left:574px"><h4>Other Links</h4><ul><li>About Us</li><li>Terms &amp; Conditions</li><li>FAQs</li><li>Gallery</li></ul></div>
    <div class="abs fcol info" style="top:30px;left:813px;width:300px"><h4>Contact Info</h4>
      <ul>
        <li><svg width="14" height="18"><path d="M7 1C3.5 1 1 3.6 1 7c0 4 6 10 6 10s6-6 6-10c0-3.4-2.5-6-6-6z" fill="#eb3d1f"/><circle cx="7" cy="7" r="2.2" fill="#111"/></svg><span style="font-size:14.5px">418 Cedar Yard Ln Suite 2, Brookfield, TX 75990, United States</span></li>
        <li><svg width="14" height="16"><path d="M3 1l3 3-2 2c1 2 3 4 5 5l2-2 3 3-2 2C6 14 1 9 1 3z" fill="#eb3d1f"/></svg><span style="font-size:14.5px">555.014.2280</span></li>
        <li><svg width="14" height="14"><rect x="1" y="3" width="12" height="9" fill="#eb3d1f"/><polyline points="1,3 7,8 13,3" fill="none" stroke="#111" stroke-width="1.2"/></svg><span style="font-size:14.5px">HaldenAutomotiveLLC@example.com</span></li>
        <li><svg width="14" height="14"><rect x="1" y="3" width="12" height="9" fill="#eb3d1f"/><polyline points="1,3 7,8 13,3" fill="none" stroke="#111" stroke-width="1.2"/></svg><span style="font-size:14.5px">Hours of Operation M-F &nbsp;8:30–6pm</span></li>
      </ul>
    </div>
    <div class="abs" style="top:278px;left:99px;font-size:15px">©Copyright 2024 Halden Automotive. All Rights Reserved.</div>
  </footer>
  <div class="social" style="left:902px"></div>
  <div class="social" style="left:954px"></div>
  <div class="social" style="left:1007px"></div>
  <div class="social" style="left:1060px"></div>

</div>
</body>
</html>
```